Rancho Verbena Wine Bottle Label

Hello! We are looking for a wine bottle label design for our private, family winery located in Chico, CA. The name of our home/ranch/vineyard is Rancho Verbena ('the exit'), which is inspired by our hilltop location, panoramic views of the valley, and sensation of escaping from the busy world below.

We planted our vineyard in 2011 and are now bottling our first harvest from fall of 2013. We planted all Italian varietals on our land: syrah, primitivo, and montepulciano. The wine we make is the culmination of all the love, support and effort poured into the process by our family and friends.

The task at hand: we are looking for a clean, simple front and back wine label design.

Front Label Content:
RV and/or Rancho Verbena
Estate Grown
Chico, CA
Varietal (use Syrah for placeholder)
Year (use 2013 for placeholder)

Back Label Content:
Running list of names of all family and friends who have participated in the process (use a text fill for placeholder)

Aesthetic Description:
Simple, clean, contemporary, text based design (see attached logo idea, Image #1)
Like the brown paper with stamped lettering look & feel
Like the classic clear label with gold lettering look & feel
Option to incorporated a simple background image/sketch of the view overlooking the valley (see attached Image #2 and #3)
Additional inspirational images attached for reference (Images #3- )

General Size Requirement:
Front Label - 4"tall by 3 1/2" wide
Back Label - 4"tall by 3 1/2" wide

Format:
Please submit Photoshop or Illustrator or InDesign Files and PDF/EPS Files.

```html
<!DOCTYPE html>
<html lang="en">
<head>
<meta charset="utf-8">
<title>Rancho Verbena — Back Label</title>
<link rel="stylesheet" href="https://fonts.googleapis.com/css2?family=Cagliostro&display=swap">
<style>
  :root {
    --kraft: #dcbb87;
    --kraft-light: #e2c492;
    --kraft-dark: #d2b07a;
    --vine-green: #6a863a;
    --verbena-purple: #93358f;
  }
  html, body {
    margin: 0;
    padding: 0;
    overflow: hidden;
  }
  body {
    width: 1050px;
    height: 1200px;
  }
  .back-label {
    position: relative;
    width: 1050px;
    height: 1200px;
    overflow: hidden;
    background:
      radial-gradient(ellipse at 30% 20%, var(--kraft-light) 0%, transparent 60%),
      radial-gradient(ellipse at 75% 85%, var(--kraft-dark) 0%, transparent 65%),
      var(--kraft);
    font-family: "Cagliostro", "Trebuchet MS", sans-serif;
  }
  .label-frame {
    position: absolute;
    left: 0;
    top: 0;
    width: 1050px;
    height: 1200px;
  }
  .monogram {
    position: absolute;
    left: 0;
    right: 0;
    top: 70px;
    margin: 0;
    text-align: center;
    font-family: "Cagliostro", "Trebuchet MS", sans-serif;
    font-weight: 400;
    font-size: 230px;
    line-height: 260px;
    letter-spacing: -6px;
    color: var(--vine-green);
  }
  .contributors {
    position: absolute;
    left: 0;
    right: 0;
    top: 378px;
    margin: 0;
    padding: 0;
    list-style: none;
    text-align: center;
    color: var(--verbena-purple);
    font-size: 47px;
    line-height: 60px;
    letter-spacing: 0.5px;
  }
</style>
</head>
<body>
  <main class="back-label">
    <svg class="label-frame" viewBox="0 0 1050 1200" aria-hidden="true">
      <path d="M75 300 V1070 Q75 1115 120 1115 H930 Q975 1115 975 1070 V300"
            fill="none" stroke="var(--vine-green)" stroke-width="3"/>
    </svg>

    <h1 class="monogram">RV</h1>

    <ul class="contributors">
      <li>First Name Last Name</li>
      <li>First Name Last Name</li>
      <li>First Name Last Name</li>
      <li>First Name Last Name</li>
      <li>First Name Last Name</li>
      <li>First Name Last Name</li>
      <li>First Name Last Name</li>
      <li>First Name Last Name</li>
      <li>First Name Last Name</li>
      <li>First Name Last Name</li>
      <li>First Name Last Name</li>
    </ul>
  </main>
</body>
</html>
```